Website redesign for a technology and engineering company

We'd like to redesign our website which can be found on quorvane.co.nz
!! Please find the designers brief as an uploaded file with all details in there!!
The main purpose for redesign is:
>change of services offered
>old website not very user friendly to maintain or update
Key requirements:
>visually appealing
>easy to navigate
>simple and easy to read
>responsive
>mobile device compatibility
>integrating best SEO practice
All the details are in the attached designer brief document.

```html
<!DOCTYPE html>
<html lang="en">
<head>
<meta charset="utf-8">
<title>Quorvane — Precision. Efficiency. Clarity.</title>
<link rel="stylesheet" href="https://fonts.googleapis.com/css2?family=Lexend:wght@400;500;600;700&family=Inter:wght@400;500;600&display=swap">
<style>
:root{
  --blue:#3d6ff2;
  --blue-soft:#dbe3fb;
  --ink:#111318;
  --text:#2a2d33;
  --muted:#8a8f98;
  --bg-grey:#f1f2f4;
  --white:#ffffff;
  --black:#000000;
  --line:#d9dce1;
}
*{margin:0;padding:0;box-sizing:border-box}
html,body{width:1200px;height:3757px;overflow:hidden}
body{position:relative;background:var(--white);font-family:"Inter",sans-serif;color:var(--text)}
.abs{position:absolute}
.head{font-family:"Lexend",sans-serif;font-weight:600;color:var(--ink)}
.accent{color:var(--blue)}
.btn{position:absolute;background:var(--blue);color:var(--white);font-family:"Lexend",sans-serif;font-size:12px;display:flex;align-items:center;justify-content:center}
.layer{position:absolute;left:0;width:1200px}

/* top bar */
.social-dot{position:absolute;width:24px;height:24px;border-radius:50%;border:1.5px solid var(--white)}
.topbar-text{position:absolute;color:var(--white);font-size:11px;top:10px}
.nav{position:absolute;left:150px;top:36px;width:900px;height:69px;background:var(--white)}
.brand{font-family:"Lexend",sans-serif;font-weight:600;color:var(--ink);display:flex;align-items:center;gap:10px}
.brand-mark{background:var(--ink);border-radius:50%}
.nav-link{position:absolute;top:27px;font-family:"Lexend",sans-serif;font-size:11px;color:var(--ink)}

/* hero */
.hero-photo{left:0;top:0;height:730px;background:linear-gradient(180deg,#2f6fd0 0%,#6aa0df 18%,#8a8a7a 38%,#6f6656 60%,#8e8a82 80%,#a7a39c 100%)}
.hero-title{left:147px;top:228px;font-size:56px;line-height:59px;color:var(--white);font-family:"Lexend",sans-serif;font-weight:600}

/* about */
.eyebrow{font-family:"Lexend",sans-serif;font-size:17px;color:var(--blue)}
.about-copy{left:607px;width:440px}

/* services */
.tab{position:absolute;top:1560px;font-family:"Lexend",sans-serif;font-size:12.5px;color:var(--muted);display:flex;align-items:center;gap:8px}
.tab-icon{width:18px;height:18px;border:1.5px solid currentColor;border-radius:4px}
.service-list{list-style:none;left:226px;top:1704px;font-size:13.5px;line-height:26.2px;color:var(--text)}
.service-list li::before{content:"• ";color:var(--blue)}

/* case studies */
.case-photo{top:2277px;width:419px;height:289px}
.case-card{top:2522px;width:381px;height:241px;background:var(--white);box-shadow:0 8px 24px rgba(0,0,0,.08);padding:28px 23px 0 23px}
.case-card h3{font-family:"Lexend",sans-serif;font-weight:500;font-size:15px;line-height:23px;color:var(--ink);margin-bottom:12px}
.case-card p{font-size:10.6px;line-height:20.4px;color:var(--text)}
.case-arrow{position:absolute;right:0;bottom:0;width:42px;height:42px;border-radius:50% 50% 0 50%;background:var(--blue)}

/* contact */
.contact-item{left:144px;display:flex;gap:16px}
.contact-item .ico{width:40px;height:40px;position:relative}
.contact-item .lab{font-size:11.5px;font-family:"Lexend",sans-serif;color:var(--ink);margin-bottom:4px}
.contact-item .val{font-size:10.5px;line-height:16px}
.form-card{left:633px;top:2989px;width:417px;height:500px;background:var(--white)}
.field-label{position:absolute;left:35px;font-size:11px;color:var(--ink)}
.field{position:absolute;left:35px;width:345px;border:1px solid var(--line);box-shadow:0 2px 6px rgba(0,0,0,.05);font-size:11px;font-style:italic;color:var(--muted);padding:10px 14px}
.field svg{position:absolute;right:12px;top:11px}

/* footer */
.sub-input{left:566px;top:3555px;width:280px;height:41px;background:var(--white);font-size:11px;font-style:italic;color:var(--ink);padding:13px 18px}
.foot-social{position:absolute;top:3629px;width:30px;height:30px;border-radius:50%;border:1.5px solid var(--white)}
</style>
</head>
<body>

<!-- HERO -->
<div class="layer abs hero-photo" role="img" aria-label="Solar powered GNSS monitoring station on a rocky alpine ridge with mountains behind"></div>

<svg class="layer" style="top:560px" width="1200" height="250" viewBox="0 560 1200 250" aria-hidden="true">
  <polygon points="0,690 751,583 1200,735 1200,810 0,810" fill="#ffffff"/>
  <polygon points="0,680 751,573 1200,735 1200,742 751,592 0,688" fill="#3d6ff2"/>
</svg>

<div class="social-dot" style="left:150px;top:5px"></div>
<div class="social-dot" style="left:185px;top:5px;background:var(--blue);border-color:var(--blue)"></div>
<div class="social-dot" style="left:218px;top:5px"></div>
<div class="social-dot" style="left:252px;top:5px"></div>
<svg class="abs" style="left:288px;top:10px" width="13" height="13" viewBox="0 0 24 24" aria-hidden="true"><path d="M6.6 10.8a15 15 0 0 0 6.6 6.6l2.2-2.2a1 1 0 0 1 1-.25 11.4 11.4 0 0 0 3.6.6 1 1 0 0 1 1 1V20a1 1 0 0 1-1 1A17 17 0 0 1 3 4a1 1 0 0 1 1-1h3.5a1 1 0 0 1 1 1c0 1.25.2 2.45.6 3.6a1 1 0 0 1-.25 1z" fill="#fff"/></svg>
<span class="topbar-text" style="left:306px">(123) 456 7890</span>
<svg class="abs" style="left:928px;top:7px" width="20" height="20" viewBox="0 0 24 24" aria-hidden="true"><path d="M4 14v-2a8 8 0 0 1 16 0v2" stroke="#fff" stroke-width="2" fill="none"/><rect x="3" y="13" width="4" height="6" rx="1.5" fill="#fff"/><rect x="17" y="13" width="4" height="6" rx="1.5" fill="#fff"/></svg>
<span class="topbar-text" style="left:958px">Customer Support</span>

<nav class="nav">
  <div class="brand abs" style="left:25px;top:18px;font-size:27px"><span class="brand-mark" style="width:22px;height:22px"></span>Quorvane</div>
  <span class="nav-link" style="left:392px">Home</span>
  <span class="nav-link" style="left:454px">Services Offered</span>
  <span class="nav-link" style="left:578px">Case Studies</span>
  <span class="nav-link" style="left:681px">About Us</span>
  <span class="btn" style="left:761px;top:15px;width:113px;height:39px">Get In Touch</span>
</nav>

<h1 class="abs hero-title">Precision.<br>Efficiency.<br>Clarity.</h1>
<span class="btn" style="left:150px;top:432px;width:111px;height:37px">Get In Touch</span>

<!-- ABOUT -->
<svg class="abs" style="left:0;top:700px" width="1200" height="560" viewBox="0 700 1200 560" aria-hidden="true">
  <polygon points="121,730 560,978 121,1240" fill="#ffffff" style="filter:drop-shadow(0 10px 30px rgba(0,0,0,.12))"/>
  <polygon points="448,740 448,855 345,790" fill="#dbe3fb"/>
  <polygon points="433,714 433,835 328,775" fill="#3d6ff2"/>
  <polygon points="22,1088 22,1190 70,1155" fill="#dbe3fb"/>
  <polygon points="28,1078 28,1178 77,1145" fill="#3d6ff2"/>
  <polygon points="988,1195 988,1255 935,1225" fill="#dbe3fb"/>
  <polygon points="980,1182 980,1245 928,1212" fill="#3d6ff2"/>
</svg>
<div class="abs" style="left:141px;top:747px;width:398px;height:461px;clip-path:polygon(0 0,100% 50%,0 100%);background:linear-gradient(135deg,#8fa7c9 0%,#c66a3a 55%,#e0632a 100%)" role="img" aria-label="Field technician in high-visibility orange shirt on a mountain site"></div>

<div class="abs about-copy" style="top:823px">
  <div class="eyebrow">ABOUT</div>
  <h2 class="head" style="font-size:37px;line-height:44px;letter-spacing:.5px">QUORVANE</h2>
  <div style="width:61px;height:3px;background:var(--blue);margin-top:4px"></div>
  <p style="font-size:13px;line-height:20.5px;margin-top:22px">Welcome To Quorvane, Your Reliable Partner In Delivering Innovative Solutions. Our Team Of Skilled Professionals Is Committed To Excellence, Ensuring Every Project Is Handled With Precision, Efficiency, And Integrity.</p>
  <p style="font-size:11px;line-height:20.5px;margin-top:10px">We Solve Problems In The Field, Build Robust Infrastructure, And Deliver Accurate Data To Our Clients. Let Us Help You Achieve Your Goals With Our Tailored, Sustainable Solutions And Exceptional Service.</p>
</div>
<span class="btn" style="left:607px;top:1101px;width:110px;height:35px">Get In Touch</span>

<!-- SERVICES -->
<div class="layer abs" style="top:1260px;height:1000px;background:var(--bg-grey)"></div>
<svg class="layer" style="top:1250px" width="1200" height="200" viewBox="0 1250 1200 200" aria-hidden="true">
  <polygon points="0,1250 1200,1250 1200,1312 452,1422 0,1268" fill="#ffffff"/>
  <polygon points="30,1268 452,1410 1200,1310 1200,1318 452,1430 30,1276" fill="#3d6ff2"/>
</svg>

<h2 class="abs head" style="left:0;width:1200px;text-align:center;top:1490px;font-size:29px">
  <span class="accent">OUR</span> SERVICES</h2>
<div class="abs" style="left:150px;top:1600px;width:900px;height:1px;background:var(--line)"></div>
<div class="abs" style="left:467px;top:1558px;width:266px;height:42px;background:var(--blue-soft)"></div>
<div class="abs" style="left:467px;top:1598px;width:266px;height:3px;background:var(--blue)"></div>
<div class="tab" style="left:274px;top:1560px;height:20px"><span class="tab-icon" style="border-radius:50%"></span>Fieldwork Solutions</div>
<div class="tab" style="left:492px;height:20px;color:var(--ink)"><span class="tab-icon" style="color:var(--blue)"></span>Positioning And Monitoring</div>
<div class="tab" style="left:765px;height:20px"><span class="tab-icon"></span>Design And Prototyping</div>

<h3 class="abs head" style="left:226px;top:1665px;font-size:18px;font-weight:500">Positioning And <span class="accent">Monitoring</span></h3>
<ul class="abs service-list">
  <li>Real-Time Kinematic (RTK) Solutions</li>
  <li>Custom GNSS Base Stations</li>
  <li>NTRIP Service</li>
  <li>Tailored Monitoring Solutions</li>
  <li>Environmental Monitoring</li>
  <li>Robust Communication Systems</li>
  <li>Internet Of Things (IoT) Integration</li>
  <li>Solar Powered Systems</li>
  <li>Smart Sensor Networks</li>
</ul>
<span class="btn" style="left:226px;top:1958px;width:111px;height:38px">Get In Touch</span>

<svg class="abs" style="left:610px;top:1630px" width="400" height="400" viewBox="610 1630 400 400" aria-hidden="true">
  <polygon points="809,1633 977,1730 977,1924 809,2021 641,1924 641,1730" fill="#ffffff" style="filter:drop-shadow(0 8px 20px rgba(0,0,0,.12))"/>
</svg>
<div class="abs" style="left:645px;top:1660px;width:328px;height:334px;clip-path:polygon(50% 0,100% 25%,100% 75%,50% 100%,0 75%,0 25%);background:linear-gradient(180deg,#9fb4c8 0%,#5f7f4a 40%,#7d7f78 70%,#5a5f66 100%)" role="img" aria-label="Surveyor beside a solar powered GNSS base station"></div>

<!-- CASE STUDIES -->
<svg class="layer" style="top:2060px" width="1200" height="200" viewBox="0 2060 1200 200" aria-hidden="true">
  <polygon points="0,2187 751,2078 1200,2231 1200,2260 0,2260" fill="#ffffff"/>
  <polygon points="0,2180 751,2070 1170,2228 1162,2230 751,2090 0,2190" fill="#3d6ff2"/>
</svg>
<h2 class="abs head" style="left:0;width:1200px;text-align:center;top:2212px;font-size:29px"><span class="accent">CASE</span> STUDIES</h2>
<div class="abs" style="left:599px;top:2280px;width:1px;height:480px;background:#eceef1"></div>

<div class="abs case-photo" style="left:150px;background:linear-gradient(180deg,#2f63c8 0%,#6f9ae0 45%,#b9b6ae 70%,#9c978e 100%)" role="img" aria-label="Solar powered camera installation on a rocky alpine ridge"></div>
<div class="abs case-card" style="left:169px">
  <h3>Remote Camera Installation In<br>Alpine Environment</h3>
  <p>Successful Installation Of Advanced Camera Systems In The Challenging And Remote Alpine Regions Of Fiordland. This Installation Supports Terravista Pty Ltd In Their Environmental Monitoring Efforts, Providing High-Quality Imagery And Data To The Alpine Lands Authority From One Of The Most Rugged And Inaccessible Areas In New Zealand.</p>
  <span class="case-arrow"></span>
  <svg class="abs" style="right:12px;bottom:12px" width="16" height="16" viewBox="0 0 16 16" aria-hidden="true"><path d="M3 13L13 3M6 3h7v7" stroke="#fff" stroke-width="1.4" fill="none"/></svg>
</div>

<div class="abs case-photo" style="left:631px;background:linear-gradient(180deg,#c9d3dc 0%,#aab8c4 35%,#6e8f4a 60%,#5c7d3a 100%)" role="img" aria-label="Surveying instrument on a tripod in a field with a radio dish behind"></div>
<div class="abs case-card" style="left:650px">
  <h3>GNSS CORS Station Upgrade<br>And Survey</h3>
  <p>Upgrade And Reference Mark Survey Of GNSS Continuously Operating Reference Stations (CORS) For The NGRA Positioning Network. This Project Enhanced The Accuracy And Reliability Of The NGRA Positioning Network, Crucial For A Wide Range Of Applications Including Land Surveying, Construction, And Geospatial Research.</p>
  <span class="case-arrow"></span>
  <svg class="abs" style="right:12px;bottom:12px" width="16" height="16" viewBox="0 0 16 16" aria-hidden="true"><path d="M3 13L13 3M6 3h7v7" stroke="#fff" stroke-width="1.4" fill="none"/></svg>
</div>

<svg class="abs" style="left:578px;top:2792px" width="46" height="10" viewBox="0 0 46 10" aria-hidden="true">
  <circle cx="5" cy="5" r="3.5" fill="#cfd3da"/><circle cx="17" cy="5" r="3.5" fill="#3d6ff2"/><circle cx="29" cy="5" r="3.5" fill="#cfd3da"/><circle cx="41" cy="5" r="3.5" fill="#cfd3da"/>
</svg>

<!-- CONTACT -->
<div class="layer abs" style="top:2820px;height:937px;background:var(--bg-grey)"></div>
<svg class="layer" style="top:2760px" width="1200" height="200" viewBox="0 2760 1200 200" aria-hidden="true">
  <polygon points="0,2760 1200,2760 1200,2821 437,2931 0,2777" fill="#ffffff"/>
  <polygon points="30,2780 437,2920 1200,2815 1200,2824 437,2940 30,2790" fill="#3d6ff2"/>
</svg>

<h2 class="abs head" style="left:144px;top:3028px;font-size:28px"><span class="accent">CONTACT</span> DETAILS</h2>
<p class="abs" style="left:144px;top:3073px;width:440px;font-size:10.8px;line-height:20px">Lorem Ipsum Odor Amet, Consectetuer Adipiscing Elit. Cubilia Montes Libero Sagittis Torquent Purus Platea.Facilisi Donec Habitasse Feugiat Semper.</p>

<div class="abs contact-item" style="top:3130px">
  <div class="ico"><svg width="40" height="40" viewBox="0 0 40 40" aria-hidden="true"><circle cx="14" cy="22" r="12" fill="#dbe3fb"/><rect x="14" y="6" width="16" height="26" fill="none" stroke="#111318" stroke-width="1.4"/><path d="M18 11h3M24 11h3M18 16h3M24 16h3M18 21h3M24 21h3" stroke="#111318" stroke-width="1.4"/></svg></div>
  <div><div class="lab">Head Office</div><div class="val">123 Lorem Ipsum Odor Ametconsectetuer<br>Adipiscing Elit. Cubilia Montes.</div></div>
</div>
<div class="abs contact-item" style="top:3202px">
  <div class="ico"><svg width="40" height="40" viewBox="0 0 40 40" aria-hidden="true"><circle cx="14" cy="22" r="12" fill="#dbe3fb"/><path d="M8 16l14-9 14 9v14H8z" fill="none" stroke="#111318" stroke-width="1.4"/><circle cx="22" cy="20" r="4" fill="none" stroke="#111318" stroke-width="1.4"/></svg></div>
  <div><div class="lab">Email Address</div><div class="val">hi@quorvane.co.nz</div></div>
</div>
<div class="abs contact-item" style="top:3266px">
  <div class="ico"><svg width="40" height="40" viewBox="0 0 40 40" aria-hidden="true"><circle cx="14" cy="22" r="12" fill="#dbe3fb"/><path d="M12 9l5 5-3 3a14 14 0 0 0 9 9l3-3 5 5-4 4C17 32 8 23 8 13z" fill="none" stroke="#111318" stroke-width="1.4"/></svg></div>
  <div><div class="lab">Phone Number</div><div class="val">(123) 456 7890</div></div>
</div>
<div class="abs brand" style="left:150px;top:3345px;font-size:44px;gap:14px"><span class="brand-mark" style="width:36px;height:36px"></span>Quorvane</div>

<!-- FOOTER BACKGROUND -->
<svg class="layer" style="top:3440px" width="1200" height="317" viewBox="0 3440 1200 317" aria-hidden="true">
  <polygon points="0,3540 820,3470 1200,3620 1200,3757 0,3757" fill="#000000"/>
  <polygon points="0,3525 820,3455 1200,3600 1200,3610 820,3466 0,3535" fill="#3d6ff2"/>
</svg>

<form class="abs form-card">
  <p class="abs head" style="left:0;width:417px;text-align:center;top:38px;font-size:13.5px;font-weight:500;line-height:22px">Fill In This Form Or Send Us An Email<br>With Your Inquiry</p>
  <span class="field-label" style="top:92px">Full Name</span>
  <div class="field" style="top:108px;height:33px">Enter Your Name<svg width="12" height="12" viewBox="0 0 12 12" aria-hidden="true"><circle cx="6" cy="4" r="2.5" fill="#555"/><path d="M1.5 11a4.5 4.5 0 0 1 9 0z" fill="#555"/></svg></div>
  <span class="field-label" style="top:150px">Phone No</span>
  <div class="field" style="top:166px;height:33px">123 456 7890<svg width="12" height="12" viewBox="0 0 24 24" aria-hidden="true"><path d="M6.6 10.8a15 15 0 0 0 6.6 6.6l2.2-2.2a1 1 0 0 1 1-.25 11.4 11.4 0 0 0 3.6.6 1 1 0 0 1 1 1V20a1 1 0 0 1-1 1A17 17 0 0 1 3 4a1 1 0 0 1 1-1h3.5a1 1 0 0 1 1 1c0 1.25.2 2.45.6 3.6a1 1 0 0 1-.25 1z" fill="#555"/></svg></div>
  <span class="field-label" style="top:210px">Email Address</span>
  <div class="field" style="top:224px;height:35px">info@mailbox.nz<svg width="12" height="12" viewBox="0 0 12 12" aria-hidden="true"><rect x="0.5" y="2" width="11" height="8" rx="1" fill="#555"/><path d="M1 3l5 4 5-4" stroke="#fff" fill="none"/></svg></div>
  <span class="field-label" style="top:270px">Message</span>
  <div class="field" style="top:283px;height:125px">Type Your Message Here!<svg width="12" height="12" viewBox="0 0 12 12" aria-hidden="true"><circle cx="6" cy="6" r="5" fill="#555"/></svg></div>
  <span class="btn" style="left:35px;top:424px;width:345px;height:38px;font-size:11px">Submit Now</span>
</form>

<h2 class="abs" style="left:354px;top:3549px;font-family:'Lexend',sans-serif;font-weight:500;font-size:20px;line-height:26px;color:var(--white)">SUBSCRIBE TO<br>OUR EMAIL</h2>
<div class="abs sub-input">Enter Your Email</div>
<svg class="abs" style="left:809px;top:3562px" width="28" height="28" viewBox="0 0 28 28" aria-hidden="true"><circle cx="14" cy="14" r="13" fill="#3d6ff2"/><path d="M9 19L19 9M12 9h7v7" stroke="#fff" stroke-width="1.6" fill="none"/></svg>

<div class="foot-social" style="left:524px"></div>
<div class="foot-social" style="left:565px;background:var(--blue);border-color:var(--blue)"></div>
<div class="foot-social" style="left:605px"></div>
<div class="foot-social" style="left:645px"></div>
<div class="abs" style="left:150px;top:3689px;width:900px;height:1px;background:#333"></div>
<p class="abs" style="left:0;width:1200px;text-align:center;top:3710px;font-size:11px;color:var(--white)">Copyright © Quorvane 2024. All Rights Reserved.</p>

</body>
</html>
```